FALKENHOF KONTOR KAFFEECATERING AUF MESSEN & EVENTS
Wir bieten ein hochwertiges Barista Catering inklusive komplettem Messe-Full- service an. Unser professionell geschultes Barista-Team sorgt für optimalen Kaffeege- nuss auf Messen, Kongressen und Events aller Art. Der elegante Abschluss mit einem Muster auf der Tasse, genannt „Latte Art“ , ist das Highlight unserer Dienstleistung.
Ob fest integriert im Messestand, als mobi- le Espressobar mit eigener Theke oder als Coffeebike- wir haben für jeden Anlass die passende Variante.
Branden Sie unser Equipment mit Ihrem Firmenlogo! Gerne beraten wir Sie hierzu.
HOSTESSENAGENTUR
Wählen Sie aus über 8.000 Hostessen und und mehr als 20 Sprachen! Unsere Hostes- sen und Hosts begleiten Sie auf:
• Messen
• Kongresse
• VIP-Veranstaltungen • Promotion
• Events aller Art
COCKTAIlS & SMOOTHIES MIT FIRMENlOGO
Unser mobiler Cocktailservice eignet sich für jede Art von Veranstaltung und ist eine geniale Ergänzung zu jedem Messestand.
Erweitern Sie das bestehende Cocktailan- gebot mit gebrandeten Smoothies in fünf verschiedenen Geschmacksrichtungen.
MESSECATERING
Egal ob klassische Häppchen, trendiges Finger- food oder Menüs in allen Variationen - sprechen Sie uns an!
Kurzum, unser Schwerpunkt liegt auf Barista-und Personalservice. An 3 Standorten-München, Berlin, Frankfurt.
Wir möchten gerne einen monatlichen Newsletter raussenden, den wir mittel MailChimp selber pflegen können. Nur brauchen wir eben dazu ein Design/Template was veränderbar ist.
Wir freuen uns auf tolle Designs!

```html
<!DOCTYPE html>
<html lang="de">
<head>
<meta charset="utf-8">
<title>Newsletter – Messecatering</title>
<link rel="stylesheet" href="https://fonts.googleapis.com/css2?family=EB+Garamond:wght@400;600&family=Nunito+Sans:wght@400&display=swap">
<style>
  :root {
    --page-bg: #ecebe8;
    --sheet-bg: #ffffff;
    --brand-brown: #7e5b3e;
    --button-brown: #80603f;
    --rule-grey: #9d9d9d;
    --body-text: #3a3a3a;
    --leaf-light: #7cc94e;
    --leaf-dark: #3f9a2a;
    --food-light: #e9dfd6;
    --food-dark: #c4987c;
    --news-a: #c9ccd8;
    --news-b: #4a4f57;
    --news-c: #d9d3c8;
  }
  * { box-sizing: border-box; margin: 0; padding: 0; }
  html, body {
    width: 1200px;
    height: 800px;
    overflow: hidden;
    background: var(--page-bg);
  }
  .newsletter {
    position: absolute;
    left: 320px;
    top: 0;
    width: 560px;
    height: 800px;
    background: var(--sheet-bg);
    overflow: hidden;
  }
  .leaf-decoration {
    position: absolute;
    left: 0;
    top: 0;
    width: 120px;
    height: 88px;
    background: linear-gradient(135deg, var(--leaf-light), var(--leaf-dark));
  }
  .section-title {
    font-family: "EB Garamond", serif;
    font-weight: 400;
    color: var(--brand-brown);
    text-align: center;
    font-size: 42px;
    letter-spacing: 0.5px;
    line-height: 1.1;
  }
  .catering .section-title { padding-top: 112px; }
  .title-rule {
    width: 62px;
    height: 4px;
    background: var(--rule-grey);
    margin: 14px auto 0;
  }
  .intro-text {
    font-family: "Nunito Sans", sans-serif;
    font-size: 14px;
    line-height: 1.55;
    color: var(--body-text);
    text-align: center;
    width: 470px;
    margin: 14px auto 0;
  }
  .cta-button {
    display: block;
    width: 160px;
    margin: 22px auto 0;
    padding: 11px 0 12px;
    background: var(--button-brown);
    color: #ffffff;
    font-family: "EB Garamond", serif;
    font-weight: 600;
    font-size: 17px;
    text-align: center;
    text-decoration: none;
  }
  .food-photo {
    margin-top: 28px;
    width: 560px;
    height: 250px;
    background: linear-gradient(160deg, var(--food-light), var(--food-dark));
  }
  .news .section-title { padding-top: 34px; }
  .news-strip {
    display: flex;
    margin-top: 28px;
    height: 140px;
  }
  .news-tile { flex: 1; }
  .news-tile--event { background: linear-gradient(135deg, var(--news-a), #e7d6cf); }
  .news-tile--stage { background: linear-gradient(135deg, var(--news-b), #7a7f86); }
  .news-tile--team  { background: linear-gradient(135deg, var(--news-c), #b9b2a7); }
</style>
</head>
<body>
  <main class="newsletter">
    <div class="leaf-decoration" role="img" aria-label="Frische Minzblätter als Dekoration"></div>

    <section class="catering">
      <h1 class="section-title">Messecatering</h1>
      <div class="title-rule"></div>
      <p class="intro-text">Egal ob klassische Häppchen, trendiges Finger- food oder Menüs in allen Variationen - sprechen Sie uns an!</p>
      <a class="cta-button" href="#">Jetzt informieren</a>
      <div class="food-photo" role="img" aria-label="Foto: Brothäppchen mit Schinken, Frischkäse und Dill"></div>
    </section>

    <section class="news">
      <h2 class="section-title">Aktuelles &amp; News</h2>
      <div class="title-rule"></div>
      <div class="news-strip">
        <div class="news-tile news-tile--event" role="img" aria-label="Foto: Messestand"></div>
        <div class="news-tile news-tile--stage" role="img" aria-label="Foto: Eventbühne"></div>
        <div class="news-tile news-tile--team" role="img" aria-label="Foto: Serviceteam auf der Messe"></div>
      </div>
    </section>
  </main>
</body>
</html>
```